Tradeshow display - back drop and matching podium wrap

Looking for a design for a tradeshow display 136.22" x 90.55". and there is approximately 12.25" side panels on each side here (see attached). Needs design for matching podium wrap as well (specs attached).
You can take a look at our website to get a feel on who we are.
www.brindlecrestflow.com
I've added a design I like so you get an idea of what I'm wanting here.
We do not want the Lumora logos on the banner please.
We do water treatment using ozone.

Industry/Entity Type

Agriculture

Requirements
Should not have
• the lumora logos

```html
<!DOCTYPE html>
<html lang="en">
<head>
<meta charset="utf-8">
<title>Brindlecrest Flow – Tradeshow Backdrop</title>
<link href="https://fonts.googleapis.com/css2?family=Montserrat:wght@300;400;700&family=Oswald:wght@600&family=Nunito:wght@900&display=swap" rel="stylesheet">
<style>
  :root {
    --page-bg: #dcdcdc;
    --blue-deep: #1a4f86;
    --blue-main: #1c76c0;
    --blue-photo: #2a5f92;
    --blue-dark: #16324f;
    --green-main: #2f5f3c;
    --green-dark: #1f3d28;
    --green-light: #4f7a59;
    --accent-blue: #3197dc;
    --white: #ffffff;
    --icon-white: #f3f5f3;
    --divider: #d8dde2;
    --body-text: #e6ece7;
  }
  * { margin: 0; padding: 0; box-sizing: border-box; }
  html, body {
    width: 1200px; height: 1200px; overflow: hidden;
    background: var(--page-bg);
    font-family: "Montserrat", sans-serif;
  }
  .backdrop {
    position: absolute; left: 50px; top: 220px;
    width: 1100px; height: 760px;
    overflow: hidden;
    box-shadow: 0 14px 30px rgba(0,0,0,0.18);
  }
  .hero {
    position: absolute; left: 0; top: 0; width: 100%; height: 400px;
    background: linear-gradient(90deg, var(--blue-deep) 0%, var(--blue-main) 22%, var(--blue-main) 42%, var(--blue-photo) 62%, var(--blue-dark) 100%);
  }
  .hero-photo {
    position: absolute; right: 0; top: 0; width: 560px; height: 400px;
    background:
      radial-gradient(ellipse 60% 35% at 70% 88%, rgba(30,60,110,0.95) 0%, rgba(30,60,110,0) 100%),
      radial-gradient(ellipse 55% 18% at 40% 66%, rgba(90,190,190,0.35) 0%, rgba(90,190,190,0) 100%),
      radial-gradient(ellipse 50% 45% at 55% 25%, rgba(130,180,230,0.4) 0%, rgba(130,180,230,0) 100%),
      linear-gradient(90deg, rgba(28,118,192,0) 0%, rgba(40,90,140,0.55) 40%, rgba(20,45,80,0.8) 100%);
  }
  .brand {
    position: absolute; left: 82px; top: 52px;
    display: flex; align-items: center; gap: 10px;
    color: var(--white); font-weight: 700; font-size: 34px; letter-spacing: -0.5px;
  }
  .brand-mark { width: 14px; height: 14px; background: var(--white); }
  .site-url {
    position: absolute; right: 34px; top: 106px;
    color: var(--white); font-size: 16px; font-weight: 400; letter-spacing: 0.3px;
  }
  .headline {
    position: absolute; left: 82px; top: 178px;
    color: var(--white); font-size: 58px; line-height: 66px; font-weight: 300;
    letter-spacing: -0.5px;
  }
  .headline strong { font-weight: 700; }
  .divider {
    position: absolute; left: 0; top: 400px; width: 100%; height: 3px;
    background: var(--divider);
  }
  .services {
    position: absolute; left: 0; top: 403px; width: 100%; height: 357px;
    background: linear-gradient(90deg, var(--green-dark) 0%, var(--green-main) 8%, var(--green-main) 35%, var(--green-light) 55%, var(--green-main) 75%, var(--green-main) 93%, var(--green-dark) 100%);
  }
  .service {
    position: absolute; top: 32px; width: 220px; margin-left: -110px;
    text-align: center; color: var(--white);
  }
  .service:nth-child(1) { left: 165px; }
  .service:nth-child(2) { left: 423px; }
  .service:nth-child(3) { left: 679px; }
  .service:nth-child(4) { left: 931px; }
  .service-icon {
    display: block; width: 92px; height: 98px; margin: 0 auto;
    border-radius: 18px;
    background: var(--icon-white);
  }
  .service-name {
    margin: 22px auto 0;
    width: 160px;
    font-family: "Oswald", sans-serif; font-weight: 600; font-size: 25px; line-height: 30px;
    letter-spacing: -0.3px;
    padding-bottom: 8px;
    border-bottom: 2px solid rgba(0,0,0,0.18);
  }
  .service-title {
    margin-top: 8px;
    font-family: "Nunito", sans-serif; font-weight: 900; font-size: 22px; line-height: 25px;
    color: var(--accent-blue);
  }
  .service-text {
    margin-top: 6px;
    font-size: 11px; line-height: 14px; font-weight: 300; color: var(--body-text);
  }
</style>
</head>
<body>
  <main class="backdrop">
    <section class="hero">
      <div class="hero-photo" role="img" aria-label="Photo of a young seedling in dark soil under falling water droplets"></div>
      <div class="brand"><span class="brand-mark"></span>Brindlecrest Flow</div>
      <div class="site-url">brindlecrestflow.com</div>
      <h1 class="headline">High-Quality <strong>Farm Water</strong><br><strong>Healthy High</strong><br>Performance Farms</h1>
    </section>
    <div class="divider"></div>
    <section class="services">
      <article class="service">
        <span class="service-icon" role="img" aria-label="Icon of a pig drinking from a water drop"></span>
        <div class="service-name">Swine</div>
        <h2 class="service-title">Swine Water<br>Treatment</h2>
        <p class="service-text">Quality water intake for<br>swine operations is critical to<br>both health and growth</p>
      </article>
      <article class="service">
        <span class="service-icon" role="img" aria-label="Icon of two leaves"></span>
        <div class="service-name">Plants</div>
        <h2 class="service-title">Greenhouse<br>Disinfection</h2>
        <p class="service-text">Enhance both Greenhouse<br>sanitation and plant<br>performance</p>
      </article>
      <article class="service">
        <span class="service-icon" role="img" aria-label="Icon of a dairy cow drinking from a water drop"></span>
        <div class="service-name">Dairy</div>
        <h2 class="service-title">Dairy Water<br>Treatment</h2>
        <p class="service-text">Over the years our ozone<br>has treated billions of<br>gallons of water</p>
      </article>
      <article class="service">
        <span class="service-icon" role="img" aria-label="Icon of a chicken drinking from a water drop"></span>
        <div class="service-name">Poultry</div>
        <h2 class="service-title">Poultry Water<br>Treatment</h2>
        <p class="service-text">Take a look at our new<br>Bio-Security system for<br>poultry operations</p>
      </article>
    </section>
  </main>
</body>
</html>
```